Specialized tax accounting firm needs letterhead design

We need a letterhead design for a professional services firm called R. Everett Lund Inc. The firm is essentially a very specialized tax accounting firm - instead of serving the end consumer, we support other public accounting firms in the area of Canadian and U.S. tax advisory and compliance (i.e. they call us on tax issues too complex for the general practitioner. Our byline is "Tax Support Services for Public Accounting Firms". Our letterhead should utilize our logo and be based on colours present in our logo (see file attached). The final design needs to convey professionalism and trustworthiness (we're hired by accountants after all!) while being creative and eye-catching.

I've attached:
The font used in the logo
The logo itself in a variety of file formats
A single page showing the key firm information which should be appearing in the letterhead

Please note that there is much more leather background around the logo than needs to be incorporated in the letterhead.

Industry/Entity Type

Accounting

```html
<!DOCTYPE html>
<html lang="en">
<head>
<meta charset="utf-8">
<title>R. Everett Lund Inc. — Letterhead</title>
<link href="https://fonts.googleapis.com/css2?family=Cormorant+Garamond:wght@500&display=swap" rel="stylesheet">
<style>
  :root {
    --backdrop: #e9e9ea;
    --paper: #ffffff;
    --ink-band: #121212;
    --ink-text: #1c1c1c;
    --muted: #6a6a6a;
    --silver: #e6e6e6;
    --accent-orange: #e9a33b;
  }
  * { box-sizing: border-box; margin: 0; padding: 0; }
  html, body {
    width: 1200px;
    height: 795px;
    overflow: hidden;
    background: var(--backdrop);
    font-family: "Cormorant Garamond", Georgia, serif;
    font-weight: 500;
  }
  .letterhead {
    position: absolute;
    left: 310px;
    top: 22px;
    width: 580px;
    height: 751px;
    background: var(--paper);
    box-shadow: 0 2px 10px rgba(0,0,0,0.12);
  }
  .firm-heading {
    position: absolute;
    left: 46px;
    top: 48px;
    width: 300px;
  }
  .firm-name {
    display: block;
    font-size: 24px;
    line-height: 1.1;
    color: var(--ink-text);
    white-space: nowrap;
  }
  .firm-byline {
    display: block;
    margin-top: 4px;
    font-size: 11px;
    line-height: 1.2;
    color: var(--muted);
    white-space: nowrap;
  }
  .contact-band {
    position: absolute;
    left: 0;
    right: 0;
    bottom: 24px;
    height: 56px;
    background: var(--ink-band);
    color: var(--silver);
    display: flex;
    flex-direction: column;
    justify-content: center;
    align-items: flex-end;
    padding: 0 22px;
    gap: 5px;
    font-size: 11px;
    line-height: 1.1;
    white-space: nowrap;
  }
  .contact-line span + span { margin-left: 12px; }
  .contact-label { color: var(--accent-orange); }
</style>
</head>
<body>
  <main class="letterhead">
    <header class="firm-heading">
      <span class="firm-name">R. Everett Lund Inc.</span>
      <span class="firm-byline">Canadian and U.S. tax advisory for accounting practices</span>
    </header>

    <footer class="contact-band">
      <p class="contact-line">18-340 Harbourview Drive, Halifax, Nova Scotia, Canada B3K 2M4</p>
      <p class="contact-line">
        <span><span class="contact-label">Phone:</span> 902.555.0148</span>
        <span><span class="contact-label">Fax:</span> 902.555.0196</span>
        <span><span class="contact-label">Email:</span> relund@taxadvisory.services</span>
        <span><span class="contact-label">Web:</span> www.taxadvisory.services</span>
      </p>
    </footer>
  </main>
</body>
</html>
```